Gaming Related Website

GuildWeave.com is a forum for gamers to connect online.

We would like a design for our front page.

Please feel free to include a basic logo.

Please take a look at the following sites for inspiration:
http://uk.plaryx.com/
http://eu.fraygrid.net/en/
http://www.stormvantor.com/

Target Market(s)

On-line gamers on consoles and PCs

Industry/Entity Type

Online

Requirements
Must have
• Please follow the wireframes attached.

```html
<!DOCTYPE html>
<html lang="en">
<head>
<meta charset="utf-8">
<title>GuildWeave.com</title>
<link href="https://fonts.googleapis.com/css2?family=PT+Sans:wght@400;700&display=swap" rel="stylesheet">
<style>
:root{
  --header-top:#1f2833;
  --header-bottom:#4b5769;
  --nav-active:#56637a;
  --divider:#5e6b7d;
  --ink:#222;
  --muted:#555;
  --line:#c9ced5;
  --panel:#ffffff;
  --list-bg:#e6e9ed;
  --item-bg:#f3f4f6;
  --scroll:#cfd7e2;
  --thumb:#b7c2d1;
  --dark:#232c37;
  --orange:#f39a1e;
  --orange-dark:#e27e10;
  --accent:#e0601c;
  --join:#dfe3e8;
  --footer-top:#1e2630;
  --footer-bottom:#3a4554;
  --footer-text:#c9d0da;
}
*{box-sizing:border-box;margin:0;padding:0}
html,body{width:1200px;height:1029px;overflow:hidden;background:#fff}
body{font-family:"PT Sans",sans-serif;color:var(--ink)}
.stage{position:relative;width:1024px;height:878px;transform:scale(1.171875);transform-origin:0 0}
.abs{position:absolute}

.site-header{position:absolute;left:0;top:0;width:1024px;height:100px;background:linear-gradient(var(--header-top),var(--header-bottom))}
.brand{position:absolute;left:25px;top:38px;color:#fff;font-size:22px;letter-spacing:.5px}
.main-nav{position:absolute;left:224px;top:0;height:100px;display:flex}
.main-nav a{display:flex;align-items:center;justify-content:center;text-align:center;height:100px;color:#fff;font-size:13px;text-decoration:none;border-left:1px solid var(--divider);line-height:1.3}
.main-nav a.active{background:linear-gradient(#4a566a,#5f6d84)}

.profile{left:10px;top:118px;width:218px;height:144px;border:1px solid var(--line)}
.avatar{left:6px;top:6px;width:80px;height:72px;background:linear-gradient(135deg,#c33 0%,#3b5fb5 60%,#7a8fb0)}
.profile-name{left:96px;top:11px;font-size:15px}
.profile-links{left:96px;top:32px;font-size:10px;color:var(--muted)}
.profile-tag{left:96px;top:49px;font-size:13px;color:var(--accent)}
.stats{left:3px;top:86px;width:210px;height:55px;background:var(--dark);display:flex}
.stat{flex:1;color:#fff;text-align:center;border-left:1px solid #fff;padding-top:3px}
.stat:first-child{border-left:0;flex:0 0 63px}
.stat:nth-child(2){flex:0 0 85px}
.stat b{display:block;font-weight:400;font-size:26px;line-height:30px}
.stat span{font-size:11px}

.game-list{left:10px;top:272px;width:218px;height:371px;background:var(--list-bg);border:1px solid var(--line)}
.game-item{position:absolute;left:3px;width:188px;height:43px;background:var(--item-bg);border:1px solid #c5cad1;display:flex;align-items:center;justify-content:center;font-size:15px;color:#333}
.scrollbar{position:absolute;background:var(--scroll)}
.scroll-btn{position:absolute;left:0;width:100%;height:20px;background:#e4e8ee;border:1px solid #c5cbd3}
.thumb{position:absolute;background:var(--thumb)}

.tab{position:absolute;font-size:15px;display:flex;align-items:center;justify-content:center}
.tab.on{background:#fff;border:1px solid var(--line);border-bottom:0}
.tab.off{background:var(--dark);color:#fff}
.feed-panel{left:238px;top:145px;width:550px;height:498px;border:1px solid var(--line)}
.filter{left:22px;top:23px;font-size:14px;display:flex;align-items:center;gap:6px;color:#333}
.check{display:inline-block;width:17px;height:15px;background:#e5e7ea;border:1px solid #c8ccd2;margin-left:12px}
.filter small{font-size:11px}
.feed{left:13px;top:58px;width:524px;height:429px;border:1px solid var(--line)}
.post{position:absolute;left:16px;width:464px;font-size:11px;line-height:15px;color:#333}
.post p+p{margin-top:16px}
.post .more{display:block;margin-top:4px}
.sep{position:absolute;left:14px;width:466px;height:1px;background:#c7ccd3}

.side-panel{border:1px solid var(--line)}
.row{position:absolute;left:15px;font-size:13px}
.join{position:absolute;left:164px;width:42px;height:19px;background:var(--join);border-radius:2px;font-size:11px;display:flex;align-items:center;justify-content:center}
.cta{position:absolute;height:28px;background:linear-gradient(var(--orange),var(--orange-dark));color:#fff;font-size:12px;font-weight:700;border-radius:2px;display:flex;align-items:center;justify-content:center}

.site-footer{position:absolute;left:0;top:652px;width:1024px;height:226px;background:linear-gradient(var(--footer-top),var(--footer-bottom))}
.fcol{position:absolute;top:35px;color:var(--footer-text)}
.fcol h3{font-weight:400;font-size:15px;color:#e8ecf1;margin-bottom:10px}
.fcol li{list-style:none;font-size:11px;line-height:21px}
.frule{position:absolute;left:10px;top:177px;width:1010px;height:1px;background:#4f5a69}
.copy{position:absolute;left:758px;top:192px;font-size:10px;color:#d8dde4}
</style>
</head>
<body>
<div class="stage">
  <header class="site-header">
    <div class="brand">GUILDWEAVE.COM</div>
    <nav class="main-nav">
      <a class="active" style="width:98px">Headlines</a>
      <a style="width:98px">Forum</a>
      <a style="width:105px">Communities</a>
      <a style="width:100px">Challenges</a>
      <a style="width:100px">Games info<br>and download</a>
      <a style="width:100px">Competitions</a>
      <a style="width:100px">Achievements</a>
      <a style="width:99px">Teams</a>
    </nav>
  </header>

  <section class="abs profile">
    <div class="abs avatar" role="img" aria-label="Player avatar artwork"></div>
    <div class="abs profile-name">Lazy Gourmet</div>
    <div class="abs profile-links">Edit | Logout</div>
    <div class="abs profile-tag">Gaming Starts</div>
    <div class="abs stats">
      <div class="stat"><b>16</b><span>Games</span></div>
      <div class="stat"><b>3</b><span>Communities</span></div>
      <div class="stat"><b>2</b><span>Teams</span></div>
    </div>
  </section>

  <section class="abs game-list">
    <div class="game-item" style="top:3px">All Games</div>
    <div class="game-item" style="top:49px">Far Vale</div>
    <div class="game-item" style="top:95px">Edgelands 2</div>
    <div class="game-item" style="top:141px">Assassin's Oath III</div>
    <div class="game-item" style="top:187px">Call to Arms: Dark Op 2</div>
    <div class="game-item" style="top:234px">Clan Clash 2</div>
    <div class="game-item" style="top:280px">Badge of Valor Frontliner</div>
    <div class="game-item" style="top:326px">World of Wyrmcraft</div>
    <div class="scrollbar" style="left:194px;top:0;width:23px;height:369px">
      <div class="scroll-btn" style="top:0"><svg width="21" height="18"><path d="M6 12l4.5-6 4.5 6z" fill="#333"/></svg></div>
      <div class="thumb" style="left:3px;top:22px;width:17px;height:210px"></div>
      <div class="scroll-btn" style="bottom:0"><svg width="21" height="18"><path d="M6 6l4.5 6 4.5-6z" fill="#333"/></svg></div>
    </div>
  </section>

  <div class="tab on" style="left:574px;top:114px;width:112px;height:32px;z-index:2;background:#fff">Newsfeed</div>
  <div class="tab off" style="left:686px;top:114px;width:102px;height:31px">Chats</div>
  <section class="abs feed-panel">
    <div class="abs filter">Filter By:
      <span class="check"></span><small>Notifications</small>
      <span class="check"></span><small>My Communities</small>
      <span class="check"></span><small>My Teams</small>
      <span class="check" style="margin-left:6px"></span><small>My Competitions</small>
    </div>
    <div class="abs feed">
      <div class="post" style="top:18px"><p>Prismatech eSolutions is a web service company, offering a wide range of services which range from designing and development.</p><p>New Patch is out for World of Wyrmcraft<span class="more">read more..</span></p></div>
      <div class="sep" style="top:111px"></div>
      <div class="post" style="top:124px"><p>Mini has posted in the Team hot Shots Private Board</p><p>New Patch is out for World of Wyrmcraft<span class="more">read more..</span></p></div>
      <div class="sep" style="top:206px"></div>
      <div class="post" style="top:218px"><p>We act in accordance with the Industry certified processes to deliver the best to our clients all over the world.<span class="more">read more..</span></p></div>
      <div class="sep" style="top:287px"></div>
      <div class="post" style="top:299px;left:19px"><p>Prismatech eSolutions is a professional website design company dedicated to provide excellent services.<span class="more">read more..</span></p></div>
      <div class="sep" style="top:366px"></div>
      <div class="post" style="top:377px;left:19px"><p>Progress in technology that has changed the way in which the customers<span class="more">read more..</span></p></div>
      <div class="scrollbar" style="left:498px;top:0;width:24px;height:427px">
        <div class="scroll-btn" style="top:0"><svg width="22" height="18"><path d="M7 12l4.5-6 4.5 6z" fill="#333"/></svg></div>
        <div class="thumb" style="left:2px;top:68px;width:20px;height:183px"></div>
        <div class="scroll-btn" style="bottom:0"><svg width="22" height="18"><path d="M7 6l4.5 6 4.5-6z" fill="#333"/></svg></div>
      </div>
    </div>
  </section>

  <div class="tab on" style="left:818px;top:118px;width:104px;height:29px;font-size:12px;z-index:2">Game Servers</div>
  <div class="tab off" style="left:922px;top:119px;width:95px;height:27px;font-size:12px">VOIP Channels</div>
  <section class="abs side-panel" style="left:798px;top:146px;width:219px;height:222px">
    <div class="row" style="top:15px">Stormvantor 3.........32/18</div><div class="join" style="top:14px">Join</div>
    <div class="row" style="top:41px">Wyrmcraft 2.........25/18</div><div class="join" style="top:40px">Join</div>
    <div class="row" style="top:67px">Web Runner......12/18</div><div class="join" style="top:66px">Join</div>
    <div class="row" style="top:93px">Far Vale..............12/18</div><div class="join" style="top:92px">Join</div>
    <div class="row" style="top:119px">Wyrmcraft 1.........10/18</div><div class="join" style="top:118px">Join</div>
    <div class="cta" style="left:15px;top:149px;width:117px">Add a game server</div>
  </section>

  <div class="tab on" style="left:826px;top:383px;width:109px;height:30px;font-size:13px;z-index:2">My Communities</div>
  <div class="tab off" style="left:935px;top:384px;width:82px;height:28px;font-size:13px">My Team</div>
  <section class="abs side-panel" style="left:798px;top:412px;width:219px;height:231px">
    <div class="row" style="top:18px">Game Quarry.com......8 online</div>
    <div class="row" style="top:46px">Wyrmcraft.com......2 online</div>
    <div class="row" style="top:74px">Game online.com......5 online</div>
    <div class="row" style="top:102px">Farvale.com......8 online</div>
    <div class="row" style="top:130px">Badge of valor.com......10 online</div>
    <div class="cta" style="left:8px;top:191px;width:128px">Set up a community</div>
  </section>

  <footer class="site-footer">
    <div class="fcol" style="left:42px"><h3>List of Members</h3><ul><li>1st Member goes here</li><li>IInd Member here</li><li>IIIrd Member goes here</li><li>All Member goes here</li></ul></div>
    <div class="fcol" style="left:208px"><h3>Filtered by Games</h3><ul><li>Games 1st</li><li>IInd games here</li><li>IIIrd games</li><li>More games</li></ul></div>
    <div class="fcol" style="left:364px"><h3>Team</h3><ul><li>Team name here</li><li>IInd Team here</li><li>Thrid Team</li><li>Fourth Team</li></ul></div>
    <div class="fcol" style="left:503px"><h3>Quick links</h3><ul><li>Term &amp; Conditions</li><li>Policy &amp; privacy</li><li>Support</li><li>Contact</li></ul></div>
    <div class="frule"></div>
    <div class="copy">© 2012 Companuy Name &nbsp;|&nbsp; All right reserved</div>
  </footer>
</div>
</body>
</html>
```